Swimming pool service business postcard redesign

We need a fresh post card design for our pool service business based in San Diego called Tide Sweepers. We are a family based, local residential pool cleaning and maintenance company. we need an offer to stand out, our logo, our colors, etc on a 5.5x8 inch full color post card.

```html
<!DOCTYPE html>
<html lang="en">
<head>
<meta charset="UTF-8">
<title>Tide Sweepers Postcard</title>
<link href="https://fonts.googleapis.com/css2?family=Oswald:wght@500;600;700&family=Montserrat:wght@500;600;700&display=swap" rel="stylesheet">
<style>
  :root {
    --navy: #0e2a5c;
    --navy-deep: #0a1f47;
    --blue: #1f6fc0;
    --cyan: #27b5ea;
    --pool-light: #5cb9ea;
    --pool-deep: #1c82cc;
    --orange: #e4531f;
    --orange-back: #df4a1c;
    --white: #ffffff;
    --paper: #fbfbfa;
    --stamp: #c8c8c8;
    --rule: #9aa0a6;
    --bg: #ecebe8;
    --ink: #1c1c1c;
  }
  * { margin: 0; padding: 0; box-sizing: border-box; }
  html, body { width: 1200px; height: 800px; overflow: hidden; }
  body { background: var(--bg); font-family: "Montserrat", sans-serif; position: relative; }

  .postcard { position: absolute; top: 204px; width: 570px; height: 392px; overflow: hidden; box-shadow: 0 6px 18px rgba(0,0,0,.18); }
  .postcard--front { left: 20px; background: var(--navy); }
  .postcard--back { left: 610px; background: var(--paper); }

  /* Front */
  .scene-photo { position: absolute; inset: 0 0 50px 0; background: linear-gradient(170deg, var(--pool-light) 0%, var(--pool-deep) 100%); }
  .navy-panel { position: absolute; left: 0; top: 0; width: 570px; height: 342px; }
  .brand { position: absolute; left: 22px; top: 26px; display: flex; align-items: center; gap: 10px; }
  .brand__dot { width: 44px; height: 44px; border-radius: 50%; background: var(--white); }
  .brand__name { font-family: "Oswald", sans-serif; font-weight: 700; font-size: 22px; line-height: 1.05; color: var(--white); }
  .headline { position: absolute; left: 196px; top: 28px; font-family: "Oswald", sans-serif; font-weight: 700; font-size: 31px; line-height: 1.05; color: var(--white); }
  .tagline { position: absolute; left: 198px; top: 104px; font-weight: 600; font-size: 15px; line-height: 1.2; color: var(--cyan); }
  .benefits { position: absolute; left: 30px; top: 148px; list-style: none; }
  .benefits li { display: flex; align-items: center; gap: 8px; font-weight: 500; font-size: 13px; color: var(--white); height: 20px; }
  .benefits svg { width: 13px; height: 13px; }

  .offer-ribbon { position: absolute; left: 36px; top: 212px; height: 24px; padding: 0 14px; background: var(--navy-deep); border-top: 2px solid var(--blue); font-family: "Oswald", sans-serif; font-weight: 600; font-size: 14px; letter-spacing: 1.5px; color: var(--white); line-height: 22px; z-index: 2; }
  .offer-box { position: absolute; left: 22px; top: 232px; width: 336px; height: 86px; background: var(--orange); border: 2px solid var(--white); border-radius: 8px; }
  .offer-free { position: absolute; left: 16px; top: 10px; font-family: "Oswald", sans-serif; font-weight: 700; font-size: 40px; line-height: 1; color: var(--white); }
  .offer-inspection { position: absolute; left: 16px; top: 56px; font-family: "Oswald", sans-serif; font-weight: 600; font-size: 15px; color: var(--white); }
  .offer-discount { position: absolute; right: 14px; top: 10px; width: 120px; background: var(--navy-deep); font-family: "Oswald", sans-serif; font-weight: 700; font-size: 19px; color: var(--white); text-align: center; line-height: 28px; }
  .offer-terms { position: absolute; right: 14px; top: 44px; width: 120px; font-weight: 600; font-size: 11px; line-height: 1.25; color: var(--white); text-align: center; }

  .contact-bar { position: absolute; left: 0; bottom: 0; width: 100%; height: 50px; background: var(--blue); display: flex; align-items: center; justify-content: space-around; padding: 0 16px; }
  .contact-bar__item { display: flex; align-items: center; gap: 7px; font-weight: 600; font-size: 13px; color: var(--white); }
  .contact-bar__item svg { width: 20px; height: 20px; }
  .contact-bar__divider { width: 1px; height: 24px; background: rgba(255,255,255,.6); }

  /* Back */
  .back-field { position: absolute; inset: 0; width: 570px; height: 392px; }
  .why-title { position: absolute; left: 34px; top: 62px; font-family: "Oswald", sans-serif; font-weight: 600; font-size: 21px; color: var(--white); }
  .why-underline { position: absolute; left: 34px; top: 96px; width: 210px; height: 4px; background: var(--navy); border-radius: 2px; }
  .why-copy { position: absolute; left: 34px; top: 112px; width: 280px; font-weight: 500; font-size: 12.5px; line-height: 1.45; color: var(--white); }
  .include-ribbon { position: absolute; left: 14px; top: 178px; height: 26px; padding: 0 28px 0 20px; background: var(--navy); clip-path: polygon(0 0, 100% 0, 90% 100%, 0 100%); font-family: "Oswald", sans-serif; font-weight: 600; font-size: 15px; line-height: 26px; color: var(--white); }
  .include-list { position: absolute; left: 34px; top: 218px; list-style: none; }
  .include-list li { display: flex; align-items: center; gap: 10px; height: 31px; font-weight: 600; font-size: 11.5px; color: var(--white); }
  .include-list svg { width: 22px; height: 22px; }
  .stamp-box { position: absolute; right: 26px; top: 22px; width: 68px; height: 80px; background: var(--stamp); }
  .address { position: absolute; left: 372px; top: 200px; width: 172px; }
  .address__to { font-weight: 600; font-size: 13px; color: var(--ink); }
  .address__line { position: absolute; left: 0; width: 172px; height: 1px; background: var(--rule); }
</style>
</head>
<body>

<section class="postcard postcard--front">
  <div class="scene-photo" role="img" aria-label="Photo area: pool technician mascot standing beside a sparkling backyard pool with palm trees"></div>
  <svg class="navy-panel" viewBox="0 0 570 342" aria-hidden="true">
    <path d="M0 0 H395 C425 50 430 120 410 180 C390 240 360 300 335 342 H0 Z" fill="var(--navy)"/>
  </svg>

  <div class="brand">
    <span class="brand__dot"></span>
    <span class="brand__name">Tide<br>Sweepers</span>
  </div>

  <h1 class="headline">YOUR POOL.<br>OUR PRIORITY.</h1>
  <p class="tagline">Expert Care You<br>Can Count On.</p>

  <ul class="benefits">
    <li><svg viewBox="0 0 14 14"><path d="M1 7.5 L5 11.5 L13 2.5" fill="none" stroke="#fff" stroke-width="2.4" stroke-linecap="round" stroke-linejoin="round"/></svg>Licensed &amp; Insured</li>
    <li><svg viewBox="0 0 14 14"><path d="M1 7.5 L5 11.5 L13 2.5" fill="none" stroke="#fff" stroke-width="2.4" stroke-linecap="round" stroke-linejoin="round"/></svg>Upfront &amp; Honest Pricing</li>
    <li><svg viewBox="0 0 14 14"><path d="M1 7.5 L5 11.5 L13 2.5" fill="none" stroke="#fff" stroke-width="2.4" stroke-linecap="round" stroke-linejoin="round"/></svg>Satisfaction Guaranteed</li>
  </ul>

  <div class="offer-ribbon">NEW CUSTOMER SPECIAL</div>
  <div class="offer-box">
    <span class="offer-free">FREE</span>
    <span class="offer-inspection">FIRST POOL INSPECTION</span>
    <span class="offer-discount">+ $50 OFF</span>
    <span class="offer-terms">Your First Month<br>of Service</span>
  </div>

  <footer class="contact-bar">
    <span class="contact-bar__item">
      <svg viewBox="0 0 20 20"><circle cx="10" cy="10" r="9" fill="none" stroke="#fff" stroke-width="1.5"/><path d="M7 5.5 L8.6 5.5 L9.3 8 L8.2 9 C8.8 10.4 9.7 11.3 11 11.9 L12 10.8 L14.5 11.5 L14.5 13 C14.5 13.6 14 14 13.4 14 C9.6 13.8 6.2 10.4 6 6.6 C6 6 6.4 5.5 7 5.5 Z" fill="#fff"/></svg>
      (619) 555-0148
    </span>
    <span class="contact-bar__divider"></span>
    <span class="contact-bar__item">
      <svg viewBox="0 0 20 20" fill="none" stroke="#fff" stroke-width="1.4"><circle cx="10" cy="10" r="8.5"/><ellipse cx="10" cy="10" rx="3.8" ry="8.5"/><path d="M1.5 10 H18.5 M3 5.8 H17 M3 14.2 H17"/></svg>
      tidesweeperssd.com
    </span>
    <span class="contact-bar__divider"></span>
    <span class="contact-bar__item">
      <svg viewBox="0 0 20 20"><circle cx="10" cy="10" r="9" fill="none" stroke="#fff" stroke-width="1.5"/><path d="M10 4.5 C7.7 4.5 6.2 6.2 6.2 8.2 C6.2 10.8 10 15 10 15 C10 15 13.8 10.8 13.8 8.2 C13.8 6.2 12.3 4.5 10 4.5 Z" fill="#fff"/><circle cx="10" cy="8.2" r="1.5" fill="var(--blue)"/></svg>
      Proudly Serving San Diego
    </span>
  </footer>
</section>

<section class="postcard postcard--back">
  <svg class="back-field" viewBox="0 0 570 392" aria-hidden="true">
    <polygon points="0,0 376,0 336,392 0,392" fill="var(--orange-back)"/>
  </svg>

  <h2 class="why-title">WHY CHOOSE TIDE SWEEPERS?</h2>
  <span class="why-underline"></span>
  <p class="why-copy">We Help San Diego homeowners enjoy a clean, healthy, worry-free pool without the hassle.</p>

  <div class="include-ribbon">WHAT WE INCLUDE</div>
  <ul class="include-list">
    <li><svg viewBox="0 0 22 22"><circle cx="11" cy="11" r="11" fill="var(--navy)"/><path d="M11 5 C9 8 7.5 10 7.5 12.2 A3.5 3.5 0 0 0 14.5 12.2 C14.5 10 13 8 11 5 Z" fill="none" stroke="#fff" stroke-width="1.3"/></svg>Water Testing &amp; Chemical Balancing</li>
    <li><svg viewBox="0 0 22 22"><circle cx="11" cy="11" r="11" fill="var(--navy)"/><rect x="7" y="5.5" width="8" height="11" rx="1" fill="none" stroke="#fff" stroke-width="1.3"/><path d="M9 9 H13 M9 11.5 H13 M9 14 H11.5" stroke="#fff" stroke-width="1.1"/></svg>Professional Service Reports</li>
    <li><svg viewBox="0 0 22 22"><circle cx="11" cy="11" r="11" fill="var(--navy)"/><path d="M5.5 13 C7 11.8 8.5 11.8 10 13 C11.5 14.2 13 14.2 14.5 13 C15.3 12.4 16 12.2 16.5 12.3" fill="none" stroke="#fff" stroke-width="1.3"/><path d="M13 5.5 V10.5" stroke="#fff" stroke-width="1.3"/></svg>Weekly Pool Cleaning</li>
    <li><svg viewBox="0 0 22 22"><circle cx="11" cy="11" r="11" fill="var(--navy)"/><rect x="7.5" y="6" width="7" height="10" rx="1.5" fill="none" stroke="#fff" stroke-width="1.3"/><path d="M7.5 9 H14.5 M7.5 12 H14.5" stroke="#fff" stroke-width="1.1"/></svg>Basket &amp; Filter Cleaning</li>
    <li><svg viewBox="0 0 22 22"><circle cx="11" cy="11" r="11" fill="var(--navy)"/><rect x="6" y="7" width="10" height="8" rx="1" fill="none" stroke="#fff" stroke-width="1.3"/><path d="M8 12.5 L10 10.5 L11.5 12 L14 9.5" fill="none" stroke="#fff" stroke-width="1.1"/></svg>Equipment Monitoring</li>
  </ul>

  <div class="stamp-box"></div>
  <div class="address">
    <span class="address__to">To.</span>
    <span class="address__line" style="top:12px; left:30px; width:142px;"></span>
    <span class="address__line" style="top:50px;"></span>
    <span class="address__line" style="top:88px;"></span>
    <span class="address__line" style="top:126px;"></span>
  </div>
</section>

</body>
</html>
```